A new medical waste company needs an attractive and modern flyer.

We are a new medical waste company disposing of biohazards waste, red bag waste and sharps disposal with a focus on customer service.

Background Information

Company Name
Trovik Waste

Industry
Medical waste management

Description of the organization and its target audience

We are a new medical waste company disposing of biohazardous waste, red bag waste and medical sharps.

Description

MODERN & ELEGANT HALF PAGE FLYER

Half page mailer (front and back) with a large image related to the medical field.

The Trovik Waste logo, with the company tag line “compliant waste solutions” should also be on front of the mailer.

Website (trovikwaste.com) & email (info@trovikwatse.com) on both sides of the flyer

Main headline
-Now you have options for your medical waste disposal

Who we serve
- Dentist
- Physicians
-Blood banks
-Tattoo parlors
-Assisted living facilities
-Laboratories
-Veterinarians

What we offer
-Straight forward pricing
-No hidden fees
-No long term contracts
-Free containers and red bags
-Routine scheduled pickups

Price $35.95
Updates

Remember this is a half page flyer. Please remove pricing from all future work.

Target Market(s)

- Dentist
- Physicians
-Blood banks
-Tattoo parlors
-Laboratories
-Veterinarians

Industry/Entity Type

It Company

Colors
33b8a4

Requirements
Must have
• See my website www.trovikwaste.com

```html
<!DOCTYPE html>
<html lang="en">
<head>
<meta charset="utf-8">
<title>Trovik Waste – Half Page Flyer</title>
<link rel="stylesheet" href="https://fonts.googleapis.com/css2?family=Lato:wght@300;400;700;900&display=swap">
<style>
  :root {
    --page-bg: #e4e6e6;
    --teal: #33b8a4;
    --teal-deep: #1f8f80;
    --teal-light: #7fd6c8;
    --ink: #0d0f10;
    --white: #ffffff;
    --bag-yellow: #f2d21a;
    --bag-shade: #c9a90c;
    --logo-green: #35b48f;
  }
  * { box-sizing: border-box; margin: 0; padding: 0; }
  html, body {
    width: 1200px;
    height: 800px;
    overflow: hidden;
    background: var(--page-bg);
    font-family: "Lato", sans-serif;
  }
  .flyer {
    position: absolute;
    left: 70px;
    top: 30px;
    width: 1060px;
    height: 740px;
    overflow: hidden;
    box-shadow: 0 10px 30px rgba(0,0,0,0.25);
  }
  .hero-photo {
    position: absolute;
    inset: 0;
    background:
      radial-gradient(ellipse at 30% 15%, rgba(220,245,240,0.55), transparent 45%),
      radial-gradient(ellipse at 85% 40%, rgba(20,110,98,0.55), transparent 55%),
      linear-gradient(135deg, #5cc7b6 0%, var(--teal) 45%, var(--teal-deep) 100%);
  }
  .feature-ring {
    position: absolute;
    left: 63px;
    top: 190px;
    width: 340px;
    height: 340px;
    border-radius: 50%;
    background: rgba(190,235,228,0.55);
    padding: 18px;
  }
  .feature-photo {
    width: 100%;
    height: 100%;
    border-radius: 50%;
    background:
      radial-gradient(circle at 50% 45%, var(--bag-yellow) 0%, #e8c414 45%, var(--bag-shade) 70%, #eef3f2 71%, #ffffff 100%);
  }
  .headline-block {
    position: absolute;
    left: 565px;
    top: 80px;
    width: 440px;
    color: var(--white);
  }
  .brand-name {
    font-size: 56px;
    font-weight: 900;
    line-height: 1.05;
    letter-spacing: 0.5px;
  }
  .tagline {
    font-size: 38px;
    line-height: 1.15;
    margin-top: 8px;
  }
  .tagline .light { font-weight: 300; }
  .tagline .bold { font-weight: 900; }
  .rule {
    height: 2px;
    background: rgba(255,255,255,0.8);
    margin: 20px 0 18px;
    width: 420px;
  }
  .main-message {
    font-size: 29px;
    font-weight: 300;
    line-height: 1.25;
  }
  .main-message strong { font-weight: 900; }
  .corner-band {
    position: absolute;
    inset: 0;
    width: 1060px;
    height: 740px;
  }
  .brand-mark {
    position: absolute;
    left: 700px;
    top: 595px;
    display: flex;
    align-items: center;
    gap: 18px;
  }
  .brand-mark .dot {
    width: 48px;
    height: 48px;
    border-radius: 50%;
    background: var(--logo-green);
  }
  .brand-mark .mark-name {
    color: var(--teal);
    font-size: 36px;
    font-weight: 400;
    letter-spacing: 3px;
    text-transform: uppercase;
  }
  .contact-line {
    position: absolute;
    left: 10px;
    top: 640px;
    display: flex;
    gap: 38px;
    color: var(--white);
    font-size: 23px;
    font-weight: 700;
  }
</style>
</head>
<body>
  <main class="flyer">
    <div class="hero-photo" role="img" aria-label="Surgeons in scrubs and caps working in an operating room, tinted teal"></div>

    <div class="feature-ring">
      <div class="feature-photo" role="img" aria-label="Yellow biohazard waste bags tied closed"></div>
    </div>

    <section class="headline-block">
      <h1 class="brand-name">Trovik Waste</h1>
      <p class="tagline"><span class="light">Compliant</span> <span class="bold">Waste Solutions</span></p>
      <div class="rule"></div>
      <p class="main-message"><strong>Now</strong> you have <strong>options</strong> for your <strong>medical waste</strong> disposal</p>
    </section>

    <svg class="corner-band" viewBox="0 0 1060 740" aria-hidden="true">
      <polygon points="530,740 1060,270 1060,740" fill="var(--ink)"/>
    </svg>

    <div class="brand-mark">
      <span class="dot"></span>
      <span class="mark-name">Trovik Waste</span>
    </div>

    <footer class="contact-line">
      <span class="website">www.trovikwaste.com</span>
      <span class="email">info@trovikwatse.com</span>
    </footer>
  </main>
</body>
</html>
```